VARQO Business card

Black card, double sided with company colors black, blue and white with slogan on back Your VARQO......

Industry/Entity Type

Business

```html
<!DOCTYPE html>
<html lang="en">
<head>
<meta charset="utf-8">
<title>VARQO Business Card</title>
<link rel="stylesheet" href="https://fonts.googleapis.com/css2?family=Source+Sans+3:wght@300;400;700&display=swap">
<style>
  :root {
    --card-dark: #3a3b3d;
    --card-darker: #2e2f31;
    --card-light: #4a4b4d;
    --brand-blue: #00aeef;
    --ink-white: #ffffff;
    --page: #ffffff;
  }
  * { margin: 0; padding: 0; box-sizing: border-box; }
  html, body {
    width: 1029px;
    height: 1200px;
    overflow: hidden;
    background: var(--page);
    font-family: "Source Sans 3", sans-serif;
    color: var(--ink-white);
  }
  .sheet { position: relative; width: 1029px; height: 1200px; }

  .card {
    position: absolute;
    left: 0;
    width: 1029px;
    height: 585px;
    overflow: hidden;
    background: var(--card-dark);
  }
  .card--front { top: 0; border-top-left-radius: 92px; }
  .card--back { top: 615px; border-top-right-radius: 125px; }

  .card__texture {
    position: absolute;
    inset: 0;
    background:
      radial-gradient(ellipse at 75% 20%, var(--card-light) 0%, transparent 55%),
      linear-gradient(160deg, var(--card-dark) 0%, var(--card-darker) 100%);
  }

  .brand-name {
    position: absolute;
    font-weight: 400;
    letter-spacing: 2px;
    line-height: 1;
  }
  .card--front .brand-name {
    left: 53px;
    top: 180px;
    font-size: 58px;
    color: var(--brand-blue);
  }
  .card--back .brand-name {
    left: 103px;
    top: 262px;
    font-size: 58px;
    color: var(--ink-white);
  }

  .person {
    position: absolute;
    right: 62px;
    top: 84px;
    text-align: right;
  }
  .person__name { font-size: 39px; font-weight: 700; line-height: 1.1; }
  .person__title { font-size: 34px; font-weight: 300; line-height: 1.3; }

  .contact-band {
    position: absolute;
    left: 0;
    top: 318px;
    width: 100%;
    height: 205px;
    background: var(--brand-blue);
  }
  .contact-band__address,
  .contact-band__phones {
    position: absolute;
    top: 44px;
    font-size: 30px;
    font-weight: 400;
    line-height: 40px;
    list-style: none;
  }
  .contact-band__address { left: 53px; }
  .contact-band__phones { right: 62px; }
  .contact-band__phones li { display: flex; }
  .contact-band__phones .label { width: 38px; }

  .website {
    position: absolute;
    left: 0;
    top: 523px;
    width: 100%;
    height: 62px;
    line-height: 62px;
    text-align: center;
    font-size: 29px;
    font-weight: 400;
  }

  .slogan {
    position: absolute;
    left: 123px;
    top: 438px;
    font-size: 40px;
    font-weight: 300;
    color: var(--brand-blue);
  }
</style>
</head>
<body>
<main class="sheet">
  <section class="card card--front">
    <div class="card__texture" role="img" aria-label="Dark grey background with faint curved architectural lines"></div>
    <div class="brand-name">VARQO</div>
    <div class="person">
      <div class="person__name">Daniel Reyes</div>
      <div class="person__title">General Manager</div>
    </div>
    <div class="contact-band">
      <ul class="contact-band__address">
        <li>415-88 Harbour Lane</li>
        <li>Lakeview BC V2K 4M8</li>
        <li>1.800.555.0142</li>
      </ul>
      <ul class="contact-band__phones">
        <li><span class="label">m:</span>+4075 555 910</li>
        <li><span class="label">p:</span>+4028 564 870</li>
        <li><span class="label">f:</span>+4028 564 871</li>
      </ul>
    </div>
    <div class="website">www.varqo.com</div>
  </section>

  <section class="card card--back">
    <div class="card__texture" role="img" aria-label="Dark grey background with faint curved architectural lines"></div>
    <div class="brand-name">VARQO</div>
    <div class="slogan">Your VARQO!</div>
  </section>
</main>
</body>
</html>
```